Rehab/fitness Business card design

I need a design that promotes "A ready made base for runners". services include assessment, massage, physiotherapy, pilates, suspension training, kinesiotaping in any combination.
I would like to bring the design into my website, flyers etc

Target Market(s)

athletes from beginner to elite - any age, male and female

Industry/Entity Type

Shop

Contact Information for Business Card

Ready-Made-Base for Runners
17 Parvel Crescent, Hollowmere, Tauranga
021 847 3610
gwen.farrowby@quillmail.test

Logo Text

Requirements
Nice to have
• Blue colour theme

```html
<!DOCTYPE html>
<html lang="en">
<head>
<meta charset="utf-8">
<title>Ready-Made-Base for Runners — Business Card</title>
<link rel="stylesheet" href="https://fonts.googleapis.com/css2?family=Michroma&family=PT+Sans:wght@400;700&display=swap">
<style>
  :root {
    --brand-blue: #1a6bb8;
    --card-white: #ffffff;
    --text-grey: #8a8a8a;
    --backdrop: #2e2e2e;
  }
  html, body {
    margin: 0;
    padding: 0;
    width: 1200px;
    height: 1000px;
    overflow: hidden;
    background: var(--backdrop);
  }
  .canvas {
    position: relative;
    width: 1200px;
    height: 1000px;
  }
  .card {
    position: absolute;
    left: 232px;
    width: 709px;
    background: var(--card-white);
    box-sizing: border-box;
  }
  /* Front */
  .card-front {
    top: 97px;
    height: 388px;
    border-bottom: 7px solid var(--brand-blue);
  }
  .side-tab {
    position: absolute;
    top: 71px;
    width: 20px;
    height: 71px;
    background: var(--brand-blue);
  }
  .side-tab.left { left: 0; }
  .side-tab.right { right: 0; }
  .brand-name {
    position: absolute;
    left: 40px;
    top: 71px;
    height: 71px;
    display: flex;
    align-items: center;
    margin: 0;
    font-family: "PT Sans", sans-serif;
    font-weight: 700;
    font-size: 26px;
    color: var(--brand-blue);
    line-height: 1;
    white-space: nowrap;
  }
  .person-name {
    position: absolute;
    right: 349px;
    top: 294px;
    margin: 0;
    font-family: "PT Sans", sans-serif;
    font-weight: 400;
    font-size: 32px;
    letter-spacing: -0.5px;
    color: var(--brand-blue);
  }
  .contact-list {
    position: absolute;
    left: 410px;
    top: 272px;
    margin: 0;
    padding: 0;
    list-style: none;
    font-family: "PT Sans", sans-serif;
    font-size: 13.5px;
    letter-spacing: -0.2px;
    color: var(--text-grey);
  }
  .contact-list li {
    display: flex;
    align-items: center;
    height: 28px;
  }
  .contact-icon {
    width: 22px;
    height: 16px;
    margin-right: 25px;
    fill: var(--brand-blue);
  }
  /* Back */
  .card-back {
    top: 537px;
    height: 388px;
    border: 8px solid var(--brand-blue);
    display: flex;
    align-items: center;
    justify-content: center;
  }
  .service-list {
    margin: 0;
    font-family: "Michroma", sans-serif;
    font-size: 19px;
    font-weight: 400;
    letter-spacing: 2px;
    line-height: 43px;
    text-transform: uppercase;
    text-align: center;
    color: var(--brand-blue);
    -webkit-text-stroke: 0.4px var(--brand-blue);
    white-space: nowrap;
  }
</style>
</head>
<body>
<main class="canvas">
  <section class="card card-front" aria-label="Business card front">
    <span class="side-tab left"></span>
    <span class="side-tab right"></span>
    <h1 class="brand-name">Ready-Made-Base for Runners</h1>
    <p class="person-name">Gwen Farrowby</p>
    <ul class="contact-list">
      <li>
        <svg class="contact-icon" viewBox="0 0 22 16" aria-hidden="true">
          <path d="M1 5 Q11 -1 21 5 L19 7 L15 6 L15 4 Q11 3 7 4 L7 6 L3 7 Z"/>
          <path d="M4 8 L7 6 L15 6 L18 8 L19 15 L3 15 Z"/>
        </svg>
        <span>021 847 3610</span>
      </li>
      <li>
        <svg class="contact-icon" viewBox="0 0 22 16" aria-hidden="true">
          <circle cx="11" cy="2" r="1.8"/>
          <path d="M10 4.5 L13 4.5 L14.5 9 L13.5 9.3 L12.5 6.5 L12.5 10 L14 16 L12.6 16 L11 11 L9.6 16 L8.2 16 L9.6 9.5 L9.6 7 L8.5 9.5 L7.5 9 Z"/>
        </svg>
        <span>17 Parvel Crescent, Hollowmere, Tauranga</span>
      </li>
      <li>
        <svg class="contact-icon" viewBox="0 0 22 16" aria-hidden="true">
          <path d="M1 3 L21 3 L21 14 L1 14 Z M2.5 4 L11 10 L19.5 4 Z" fill-rule="evenodd"/>
        </svg>
        <span>gwen.farrowby@quillmail.test</span>
      </li>
    </ul>
  </section>

  <section class="card card-back" aria-label="Business card back">
    <p class="service-list">
      Assessment, massage, physiotherapy,<br>
      pilates, suspension training,<br>
      kinesiotaping in any combination
    </p>
  </section>
</main>
</body>
</html>
```